Logo and Business Card Design

We are macadamia farmers with a network of operations able to deliver macadamia nuts to you!
Be it wholesale or retail supply, our production capacity, network of farms and processing facilities is able to provide reliable and secure supply of macadamia products.
We have a network of owned and contract production macadamia farms located throughout Queensland and New South Wales. Our farms are located in the lush green hinterland area of Northern New south wales and the rich and productive farmlands of the Burnett area of southern Queensland. We pride ourselves on our environmentally sensitive production systems, the ownership and pride in which our network of farmers care for their orchards and the food we produce. Collectively our farms deliver to processing facilities able to provide macadamia nut in shell and kernel in wholesale and retail quantities.
Our point of difference is our integrated supply chain, delivering paddock to plate capacity.
The enterprise is a true network in that we have combined production, processing and marketing expertise into a one stop shop!
Our design should communicate our network capacity, we are a food producer which is respectful of the land and the environment in which we operate.
Our focus is Macadamia nut production, we farm and process Macadamia's where they are a native tree.

The draft design concept we feel is too mechanical and sterile, its time for something fresh and exciting!

Environment

Pell Orchard Pty. Ltd
An Integrated Macadamia production Enterprise.

```html
<!DOCTYPE html>
<html lang="en">
<head>
<meta charset="utf-8">
<title>Pell Orchard – Business Card</title>
<link rel="stylesheet" href="https://fonts.googleapis.com/css2?family=Roboto:wght@300;400;900&display=swap">
<style>
  :root{
    --stage:#ece8e1;
    --paper:#ffffff;
    --bark:#4f2f1e;
    --leaf:#22b35a;
    --leaf-soft:#33c06b;
    --ink-light:#f3ece6;
    --foliage-dark:#1f4a1c;
    --foliage-mid:#3f7a2c;
    --foliage-light:#86b556;
  }
  *{box-sizing:border-box;margin:0;padding:0}
  html,body{width:1200px;height:885px;overflow:hidden;background:var(--stage)}
  body{position:relative;font-family:"Roboto",Arial,sans-serif}
  .card{position:absolute;width:525px;height:300px;background:var(--paper);overflow:hidden;box-shadow:0 10px 28px rgba(60,40,20,.22)}
  .card--front{left:337px;top:100px}
  .card--back{left:337px;top:485px}

  /* front */
  .brand{position:absolute;left:34px;top:42px;display:flex;align-items:center;gap:10px}
  .brand__name{font-weight:900;font-size:30px;line-height:.95;color:var(--bark);letter-spacing:.5px;text-transform:uppercase}
  .brand__dot{width:22px;height:22px;border-radius:50%;background:var(--leaf)}
  .person{position:absolute;right:34px;top:44px;text-align:right}
  .person__name{font-size:25px;font-weight:400;color:var(--bark)}
  .person__role{font-size:14px;font-weight:300;color:var(--leaf);margin-top:4px}
  .rule{position:absolute;left:0;width:100%;height:2px;background:var(--leaf)}
  .rule--top{top:152px}
  .rule--bottom{top:262px}
  .band{position:absolute;left:0;top:158px;width:100%;height:100px;background:var(--bark);display:flex;justify-content:space-between;padding:18px 30px 0 34px}
  .contacts{list-style:none;display:flex;flex-direction:column;gap:7px}
  .contacts li{display:flex;align-items:flex-start;gap:9px;color:var(--ink-light);font-size:13px;font-weight:300;line-height:1.25}
  .icon{flex:none;width:16px;height:16px;background:var(--paper);display:flex;align-items:center;justify-content:center}
  .icon svg{width:11px;height:11px;fill:var(--leaf)}

  /* back */
  .photo{position:absolute;left:0;width:100%;background:linear-gradient(120deg,var(--foliage-dark),var(--foliage-mid) 45%,var(--foliage-light) 80%,var(--foliage-mid))}
  .photo--top{top:0;height:96px}
  .photo--bottom{top:214px;height:86px}
  .stripe{position:absolute;left:0;top:96px;width:100%;height:118px;background:var(--paper);border-top:3px double var(--foliage-mid);border-bottom:3px double var(--foliage-mid);display:flex;flex-direction:column;align-items:center;justify-content:center;gap:10px}
  .stripe .brand{position:static}
  .brand--large .brand__name{font-size:40px}
  .brand--large .brand__dot{width:28px;height:28px}
  .tagline{font-size:15px;font-weight:400;color:var(--bark)}
</style>
</head>
<body>
  <section class="card card--front">
    <div class="brand">
      <span class="brand__dot"></span>
      <span class="brand__name">Pell<br>Orchard</span>
    </div>
    <div class="person">
      <p class="person__name">Daniel Whitford</p>
      <p class="person__role">Managing Director</p>
    </div>
    <div class="rule rule--top"></div>
    <div class="band">
      <ul class="contacts">
        <li><span class="icon"><svg viewBox="0 0 24 24"><path d="M6.6 10.8a15 15 0 0 0 6.6 6.6l2.2-2.2c.3-.3.7-.4 1-.2 1.1.4 2.3.6 3.6.6.6 0 1 .4 1 1V20c0 .6-.4 1-1 1A17 17 0 0 1 3 4c0-.6.4-1 1-1h3.5c.6 0 1 .4 1 1 0 1.3.2 2.5.6 3.6.1.3 0 .7-.2 1z"/></svg></span>0400 118 264</li>
        <li><span class="icon"><svg viewBox="0 0 24 24"><path d="M6 3h10v5H6zM4 9h16v9h-3v3H7v-3H4zm5 6v4h6v-4z"/></svg></span>0000 000 000</li>
        <li><span class="icon"><svg viewBox="0 0 24 24"><path d="M2 5h20v14H2zm2 2v.5l8 5.5 8-5.5V7z"/></svg></span>info@youremail.com</li>
      </ul>
      <ul class="contacts">
        <li><span class="icon"><svg viewBox="0 0 24 24"><circle cx="12" cy="12" r="9" fill="none" stroke="#22b35a" stroke-width="2.4"/><path d="M3 12h18M12 3c3 3 3 15 0 18M12 3c-3 3-3 15 0 18" fill="none" stroke="#22b35a" stroke-width="1.8"/></svg></span>www.yourwebsite.com</li>
        <li><span class="icon"><svg viewBox="0 0 24 24"><path d="M12 2a7 7 0 0 0-7 7c0 5 7 13 7 13s7-8 7-13a7 7 0 0 0-7-7zm0 9.5a2.5 2.5 0 1 1 0-5 2.5 2.5 0 0 1 0 5z"/></svg></span>Your Adress Inc 2nd Lane<br>Ave Edison, NJ 00000</li>
      </ul>
    </div>
    <div class="rule rule--bottom"></div>
  </section>

  <section class="card card--back">
    <div class="photo photo--top" role="img" aria-label="Photograph of green macadamia nuts on a branch"></div>
    <div class="stripe">
      <div class="brand brand--large">
        <span class="brand__dot"></span>
        <span class="brand__name">Pell Orchard</span>
      </div>
      <p class="tagline">An Integrated Macadamia production Enterprise</p>
    </div>
    <div class="photo photo--bottom" role="img" aria-label="Photograph of macadamia tree foliage"></div>
  </section>
</body>
</html>
```